Unique and Affordable skin care business needs new business card

I currently have business cards that were designed on this site, but I am looking for a little update to my cards. I have recently relocated to a new location and need to update that information, as well as I would like to specify that not only do I do all skin care services at a very affordable price, but I also now do eyelash extensions, which are very much in demand!! I would like to include the pictures of my current business cards for ideas on how to change them and refresh them. My business name is Glow Haven by Maren my tag line is unique and affordable skin care just for YOU.

Industry/Entity Type

Business

```html
<!DOCTYPE html>
<html lang="en">
<head>
<meta charset="utf-8">
<title>Glow Haven by Maren – Business Card</title>
<link rel="stylesheet" href="https://fonts.googleapis.com/css2?family=Bebas+Neue&family=Raleway:wght@300&family=Roboto:wght@700&display=swap">
<style>
  :root {
    --pink: #e8245f;
    --black: #000000;
    --white: #ffffff;
    --bg-light: #f3f0ee;
    --bg-mid: #d2c9c4;
    --bg-dark: #b0a299;
  }
  html, body {
    margin: 0;
    padding: 0;
    width: 1200px;
    height: 693px;
    overflow: hidden;
  }
  .card {
    position: relative;
    width: 1200px;
    height: 693px;
    overflow: hidden;
    background: linear-gradient(170deg, var(--bg-light) 0%, var(--bg-mid) 50%, var(--bg-dark) 100%);
  }
  .tagline {
    position: absolute;
    left: 177px;
    top: 65px;
    margin: 0;
    font-family: "Raleway", sans-serif;
    font-weight: 300;
    font-size: 35px;
    line-height: 1;
    letter-spacing: -0.6px;
    color: var(--pink);
    text-transform: uppercase;
    white-space: nowrap;
  }
  .services {
    position: absolute;
    left: 178px;
    top: 100px;
    margin: 0;
    font-family: "Roboto", sans-serif;
    font-weight: 700;
    font-size: 23px;
    line-height: 1;
    color: var(--pink);
    text-transform: uppercase;
    white-space: nowrap;
  }
  .brand {
    position: absolute;
    left: 764px;
    top: 262px;
    font-family: "Bebas Neue", sans-serif;
    line-height: 1;
    text-transform: uppercase;
  }
  .brand-lead {
    display: block;
    margin-left: 11px;
    font-size: 31px;
    line-height: 30px;
    color: var(--black);
  }
  .brand-name {
    display: block;
    margin-top: 1px;
    font-size: 116px;
    line-height: 89px;
    color: var(--white);
  }
  .brand-role {
    display: block;
    margin-top: 0;
    font-size: 40px;
    line-height: 35px;
    color: var(--pink);
  }
  .bars {
    position: absolute;
    left: 0;
    top: 481px;
    width: 739px;
    height: 61px;
  }
  .contact {
    position: absolute;
    left: 0;
    right: 0;
    top: 652px;
    margin: 0;
    text-align: center;
    font-family: "Bebas Neue", sans-serif;
    font-size: 31px;
    line-height: 1;
    color: var(--white);
    text-transform: uppercase;
    white-space: nowrap;
  }
</style>
</head>
<body>
  <main class="card">
    <p class="tagline">Unique and affordable skin care just for you</p>
    <p class="services">Skin care services &amp; eyelash extensions · Verdalis products</p>

    <div class="brand">
      <span class="brand-lead">Glow Haven by</span>
      <span class="brand-name">Maren<br>Holt</span>
      <span class="brand-role">Professional<br>Licensed Esthetician</span>
    </div>

    <svg class="bars" viewBox="0 0 739 61" aria-hidden="true">
      <rect x="0" y="0" width="739" height="21" fill="var(--black)"/>
      <rect x="0" y="40" width="739" height="21" fill="var(--black)"/>
    </svg>

    <p class="contact">418 Elm Avenue Fairhaven, CO 80612 555-214-738 glowhavenbymaren.com</p>
  </main>
</body>
</html>
```